Retirement Plan Advisor Bio

See the attached document and photo for content. I would like someone to design this one page flyer using my logo. This logo was designed by a designer with sketch hive. I am looking for a professional looking document. I want to he color scheme to be primarily white and gold.

Target Market(s)

Employers who offer a retirement plan

Requirements
Should not have
• The designs that I have received look more like resumes. I am interested in advertising my Retirement plan services. If anyone can change their submissions and change it to an ad for retirement plan services instead of a Bio or resume, I would prefer that.

```html
<!DOCTYPE html>
<html lang="en">
<head>
<meta charset="utf-8">
<title>Helen R. Varga – Retirement Plan Advisor</title>
<link rel="stylesheet" href="https://fonts.googleapis.com/css2?family=Open+Sans:wght@400;600;700&display=swap">
<style>
  :root {
    --gold: #d3af6c;
    --gold-deep: #a8844a;
    --gold-light: #cfb07c;
    --ink: #2f2f2f;
    --paper: #ffffff;
  }
  * { margin: 0; padding: 0; box-sizing: border-box; }
  html, body { width: 927px; height: 1200px; overflow: hidden; background: var(--paper); }
  body { font-family: "Open Sans", sans-serif; color: var(--ink); }
  .flyer { position: relative; width: 927px; height: 1200px; background: var(--paper); }

  .portrait-panel {
    position: absolute; left: 601px; top: 0; width: 259px; height: 362px;
    background: var(--gold); border-radius: 0 0 130px 130px;
  }
  .panel-brand {
    position: absolute; left: 0; right: 0; top: 54px; text-align: center;
    color: var(--paper); font-size: 14px; font-weight: 600; letter-spacing: 0.5px;
  }
  .panel-brand .brand-dot {
    display: inline-block; width: 12px; height: 12px; border-radius: 50%;
    background: var(--paper); margin-right: 7px; vertical-align: -1px;
  }
  .portrait {
    position: absolute; left: 7px; top: 108px; width: 245px; height: 245px; border-radius: 50%;
    background: radial-gradient(circle at 50% 40%, #e8d2b8 0%, #c9b59a 35%, #8ea0c2 75%, #6f84ad 100%);
  }

  .intro { position: absolute; left: 73px; top: 96px; width: 480px; }
  .intro h1 { color: var(--gold); font-size: 32px; font-weight: 700; line-height: 1.1; }
  .credentials { margin-top: 14px; font-size: 17px; line-height: 27px; }
  .mission { margin-top: 21px; font-size: 17.5px; line-height: 27px; text-align: justify; }
  .mission strong { font-weight: 700; }

  .section { position: absolute; left: 58px; width: 800px; }
  .section h2 {
    margin-left: 15px; color: var(--gold); font-size: 18.5px; font-weight: 700; line-height: 27px;
  }
  .section ul { list-style: none; }
  .section li {
    position: relative; padding-left: 15px; font-size: 17.5px; line-height: 27.3px; text-align: justify;
  }
  .section li::before {
    content: ""; position: absolute; left: 2px; top: 12px; width: 5px; height: 5px;
    border-radius: 50%; background: var(--gold);
  }
  .section .disclaimer { padding-left: 15px; font-size: 17px; line-height: 27px; }
  .specialties { top: 367px; }
  .qualifications { top: 544px; }
  .education { top: 721px; }

  .gold-band {
    position: absolute; left: 0; top: 888px; width: 927px; height: 33px;
    background: linear-gradient(90deg, #a7814a 0%, #b8955f 30%, #cdb07c 50%, #b8955f 75%, #8b7046 100%);
  }

  .contact { position: absolute; left: 86px; top: 984px; list-style: none; }
  .contact li { display: flex; align-items: flex-start; font-size: 20px; line-height: 29px; margin-bottom: 3px; }
  .contact svg { width: 20px; height: 20px; margin: 4px 18px 0 0; flex: none; }
  .divider { position: absolute; left: 374px; top: 950px; width: 1px; height: 220px; background: var(--gold); }

  .footer-brand {
    position: absolute; left: 428px; top: 1040px; display: flex; align-items: center;
    color: var(--gold-deep); font-size: 34px; font-weight: 600; letter-spacing: 0.5px; white-space: nowrap;
  }
  .footer-brand .brand-dot {
    width: 30px; height: 30px; border-radius: 50%; background: var(--gold-deep); margin-right: 14px;
  }
</style>
</head>
<body>
<main class="flyer">
  <aside class="portrait-panel">
    <div class="panel-brand"><span class="brand-dot"></span>Goldline Advisory, LLC</div>
    <div class="portrait" role="img" aria-label="Portrait photo of the advisor"></div>
  </aside>

  <header class="intro">
    <h1>About Helen R. Varga</h1>
    <p class="credentials">CFP®AIF®<br>Northmark Securities Advisor</p>
    <p class="mission">I strive to improve retirement outcomes for my plan sponsor clients and their employees through careful retirement plan design assistance, strategic and targeted communication <strong>and education , as well as continual monitoring of results.</strong></p>
  </header>

  <section class="section specialties">
    <h2>Professional Specialties</h2>
    <ul>
      <li>Over 18 years of experience in the retirement plan industry.</li>
      <li>Focused on helping plan sponsors reduce administrative burdens and fiduciary risk.</li>
      <li>Dedicated to helping employees work toward a positive retirement outcome through careful analysis of their savings rate, investment strategy and overall financial wellness.</li>
    </ul>
  </section>

  <section class="section qualifications">
    <h2>Qualifications</h2>
    <ul>
      <li>Certified Financial Planner®</li>
      <li>Accredited Investment Fiduciary®</li>
      <li>Investment Advisor Representative.</li>
      <li>Series 7, 63, and 65 Securities licenses with Northmark Securities.</li>
      <li>Holds Life and Health Insurance licenses from Illinois.</li>
    </ul>
  </section>

  <section class="section education">
    <h2>Education</h2>
    <ul>
      <li>BS Westbrook University, 1987.</li>
    </ul>
    <p class="disclaimer">*Securities and Investment Advisory Services offered through Northmark Securities Holdings, Inc, a Registered Broker/Dealer and Investment Advisor, member NSRA/SIPF.</p>
  </section>

  <div class="gold-band"></div>

  <ul class="contact">
    <li>
      <svg viewBox="0 0 20 20" aria-hidden="true"><path d="M10 1a6 6 0 0 0-6 6c0 4.5 6 12 6 12s6-7.5 6-12a6 6 0 0 0-6-6zm0 8.3A2.3 2.3 0 1 1 10 4.7a2.3 2.3 0 0 1 0 4.6z" fill="#d3af6c"/></svg>
      <span>2400 Larkfield Rd.<br>Maple Grove, IL 60999</span>
    </li>
    <li>
      <svg viewBox="0 0 20 20" aria-hidden="true"><path d="M5 2l3 3.5-1.7 2c1 2.3 2.9 4.2 5.2 5.2l2-1.7L17 14l-2 3C9 17 3 11 3 5z" fill="#d3af6c"/></svg>
      <span>(555)014.2287</span>
    </li>
    <li>
      <svg viewBox="0 0 20 20" aria-hidden="true"><path d="M2 8l8-6 8 6v10H2z" fill="#d3af6c"/><path d="M2 8l8 6 8-6" fill="none" stroke="#fff" stroke-width="1.4"/></svg>
      <span>helen.varga@northmark.com</span>
    </li>
    <li>
      <svg viewBox="0 0 20 20" aria-hidden="true"><g fill="none" stroke="#d3af6c" stroke-width="1.5"><circle cx="10" cy="10" r="8"/><ellipse cx="10" cy="10" rx="3.5" ry="8"/><path d="M2 10h16M3.5 6h13M3.5 14h13"/></g></svg>
      <span>www.helenvarga.com</span>
    </li>
  </ul>

  <div class="divider"></div>

  <div class="footer-brand"><span class="brand-dot"></span>Goldline Advisory, LLC</div>
</main>
</body>
</html>
```